Pemberly & Associates Tax Services

Need an eye catching advertisement/lead generating design for prospects interesting in professional tax planning and tax preparation services. Ideas for
Sample Advertising Language is below:

We are accepting new clients!!
We are affordable and have over 20 years of experience serving the tax needs of our clientele.

Here are a few reasons you may want to contact us:

1. You want to learn how to maximize business deductions
2. You’re a high-income earner and want to learn ways to pay less in taxes
3. You have an interest in starting a business
4. You want to maximize rental property deductions
5. You have questions about maintaining a home office
6. You want to be updated periodically on tax law changes and tax planning strategies
7. You want to be represented by a tax expert before the IRS if you are subject to an audit

References available upon request.

Target Market(s)

Individuals, small businesses and startup business

Industry/Entity Type

Tax and Accounting Industry

Requirements
Nice to have
• Would like to develop a marketing campaign that can be used periodically to digitally generate leads, build email contact list of prospective clients who want to receive tax updates.

```html
<!DOCTYPE html>
<html lang="en">
<head>
<meta charset="utf-8">
<title>Pemberly &amp; Associates Tax Services – Flyer</title>
<link rel="stylesheet" href="https://fonts.googleapis.com/css2?family=Montserrat:wght@400;500;700;800&display=swap">
<style>
  :root{
    --brand-blue:#2a5d9b;
    --brand-blue-dark:#1d4577;
    --brand-green:#2f9c5a;
    --ink:#2a3440;
    --soft-grey:#e9ecef;
    --white:#ffffff;
  }
  *{margin:0;padding:0;box-sizing:border-box;}
  html,body{width:915px;height:1200px;overflow:hidden;background:var(--white);}
  body{font-family:"Montserrat",sans-serif;color:var(--ink);}
  .flyer{position:relative;width:915px;height:1200px;background:var(--white);overflow:hidden;}

  .hero-art{position:absolute;left:0;top:0;width:915px;height:528px;}

  .brand{position:absolute;left:50px;top:78px;display:flex;align-items:center;gap:14px;}
  .brand-dot{width:44px;height:44px;border-radius:50%;background:var(--brand-blue);}
  .brand-name{font-family:"Montserrat",sans-serif;font-weight:700;font-size:25px;color:var(--brand-blue);line-height:1.15;}

  .headline{position:absolute;left:55px;top:222px;color:var(--white);line-height:57px;}
  .headline .light{display:block;font-weight:400;font-size:45px;}
  .headline .bold{display:block;font-weight:700;font-size:44px;}
  .headline .amp{font-weight:400;}
  .headline-rule{position:absolute;left:55px;top:484px;width:520px;height:2px;background:var(--white);}
  .headline-rule::before{content:"";position:absolute;left:0;top:-2px;width:143px;height:6px;background:var(--brand-green);}

  .reasons-intro{position:absolute;left:55px;top:585px;width:380px;font-size:17px;line-height:21px;color:var(--ink);}
  .reasons{position:absolute;left:55px;top:646px;width:400px;list-style:none;}
  .reasons li{position:relative;padding-left:37px;font-size:15.5px;line-height:18px;margin-bottom:11px;color:var(--ink);}
  .reasons li svg{position:absolute;left:0;top:1px;width:18px;height:18px;}

  .desk-photo{position:absolute;left:502px;top:584px;width:250px;height:128px;}

  .promise{position:absolute;left:501px;top:728px;width:360px;font-size:21px;line-height:21.5px;color:var(--brand-blue);}
  .promise strong{color:var(--brand-green);font-weight:700;}

  .cert-badge{position:absolute;left:503px;top:830px;width:232px;height:56px;}

  .contact-rule{position:absolute;left:501px;top:905px;width:251px;height:1px;background:#b9bfc6;}
  .call-label{position:absolute;left:502px;top:916px;font-size:17px;color:var(--brand-blue);}
  .call-number{position:absolute;left:500px;top:936px;font-size:31px;font-weight:700;color:var(--brand-green);letter-spacing:.5px;}

  .new-clients{position:absolute;left:0;top:997px;width:915px;height:39px;background:var(--brand-green);color:var(--white);font-weight:700;font-size:28px;text-align:center;line-height:39px;letter-spacing:.5px;}
  .footer{position:absolute;left:0;top:1036px;width:915px;height:164px;background:var(--brand-blue);color:var(--white);font-size:14.5px;}
  .footer-item{position:absolute;top:12px;display:flex;align-items:center;gap:10px;}
  .footer-item.address{left:32px;}
  .footer-item.email{left:578px;}
  .footer-item svg{width:16px;height:16px;}
</style>
</head>
<body>
<div class="flyer">

  <svg class="hero-art" viewBox="0 0 915 528" aria-hidden="true">
    <defs>
      <linearGradient id="officePhotoTone" x1="0" y1="0" x2="1" y2="1">
        <stop offset="0" stop-color="#c9d3dc"/>
        <stop offset=".5" stop-color="#8c9aa6"/>
        <stop offset="1" stop-color="#5d6670"/>
      </linearGradient>
      <linearGradient id="bandFade" x1="0" y1="0" x2="1" y2="0">
        <stop offset="0" stop-color="#2a5d9b" stop-opacity="1"/>
        <stop offset=".6" stop-color="#2a5d9b" stop-opacity=".96"/>
        <stop offset="1" stop-color="#1d4577" stop-opacity=".82"/>
      </linearGradient>
    </defs>
    <g role="img" aria-label="Photo of a smiling tax advisor at an office desk with a colleague on the phone behind him">
      <polygon points="611,0 915,0 915,340 769,528 300,528 454,199" fill="url(#officePhotoTone)"/>
    </g>
    <polygon points="0,199 472,199 769,528 0,528" fill="url(#bandFade)"/>
    <polygon points="569,0 611,0 492,160 454,199 456,160" fill="#eceeef"/>
    <polygon points="608,0 620,0 517,95 502,95" fill="var(--brand-green)"/>
    <polygon points="915,300 915,340 769,528 725,528" fill="#eceeef"/>
    <polygon points="915,413 915,428 833,528 815,528" fill="var(--brand-green)"/>
  </svg>

  <div class="brand">
    <span class="brand-dot"></span>
    <span class="brand-name">Pemberly &amp; Associates LLC</span>
  </div>

  <h1 class="headline">
    <span class="light">Professional</span>
    <span class="bold">Tax planning <span class="amp">&amp;</span></span>
    <span class="bold">Tax preparation</span>
    <span class="bold">Services</span>
  </h1>
  <div class="headline-rule"></div>

  <p class="reasons-intro">Here are a few reasons you may want to contact us:</p>
  <ul class="reasons">
    <li><svg viewBox="0 0 18 18"><circle cx="9" cy="9" r="7.5" fill="none" stroke="var(--brand-blue)" stroke-width="1.6"/><path d="M5 9l3 3 6-7" fill="none" stroke="var(--brand-green)" stroke-width="2"/></svg>You want to learn how to maximize business deductions</li>
    <li><svg viewBox="0 0 18 18"><circle cx="9" cy="9" r="7.5" fill="none" stroke="var(--brand-blue)" stroke-width="1.6"/><path d="M5 9l3 3 6-7" fill="none" stroke="var(--brand-green)" stroke-width="2"/></svg>You’re a high-income earner and want to learn ways to pay less in taxes</li>
    <li><svg viewBox="0 0 18 18"><circle cx="9" cy="9" r="7.5" fill="none" stroke="var(--brand-blue)" stroke-width="1.6"/><path d="M5 9l3 3 6-7" fill="none" stroke="var(--brand-green)" stroke-width="2"/></svg>You have an interest in starting a business</li>
    <li><svg viewBox="0 0 18 18"><circle cx="9" cy="9" r="7.5" fill="none" stroke="var(--brand-blue)" stroke-width="1.6"/><path d="M5 9l3 3 6-7" fill="none" stroke="var(--brand-green)" stroke-width="2"/></svg>You want to maximize rental property deductions</li>
    <li><svg viewBox="0 0 18 18"><circle cx="9" cy="9" r="7.5" fill="none" stroke="var(--brand-blue)" stroke-width="1.6"/><path d="M5 9l3 3 6-7" fill="none" stroke="var(--brand-green)" stroke-width="2"/></svg>You have questions about maintaining a home office</li>
    <li><svg viewBox="0 0 18 18"><circle cx="9" cy="9" r="7.5" fill="none" stroke="var(--brand-blue)" stroke-width="1.6"/><path d="M5 9l3 3 6-7" fill="none" stroke="var(--brand-green)" stroke-width="2"/></svg>You want to be updated periodically on tax law changes and tax planning strategies</li>
    <li><svg viewBox="0 0 18 18"><circle cx="9" cy="9" r="7.5" fill="none" stroke="var(--brand-blue)" stroke-width="1.6"/><path d="M5 9l3 3 6-7" fill="none" stroke="var(--brand-green)" stroke-width="2"/></svg>You want to be represented by a tax expert before the IRS if you are subject to an audit</li>
  </ul>

  <svg class="desk-photo" viewBox="0 0 250 128">
    <defs>
      <linearGradient id="deskPhotoTone" x1="0" y1="0" x2="1" y2="1">
        <stop offset="0" stop-color="#efe9e2"/>
        <stop offset=".55" stop-color="#c9b9a6"/>
        <stop offset="1" stop-color="#8f8a86"/>
      </linearGradient>
    </defs>
    <polygon points="1,1 232,1 249,19 249,127 1,127" fill="none" stroke="var(--brand-green)" stroke-width="1.5"/>
    <g role="img" aria-label="Photo of hands using a calculator over tax documents on a desk">
      <polygon points="6,6 229,6 243,21 243,122 6,122" fill="url(#deskPhotoTone)"/>
    </g>
  </svg>

  <p class="promise">We are <strong>affordable</strong> and have over <strong>20 years of experience serving</strong> the tax needs of our clientele.</p>

  <svg class="cert-badge" viewBox="0 0 232 56" role="img" aria-label="Certification badge">
    <rect x="2" y="2" width="228" height="52" fill="none" stroke="#a3a49a" stroke-width="3"/>
    <rect x="10" y="10" width="86" height="36" fill="#d8d6cb"/>
  </svg>

  <div class="contact-rule"></div>
  <p class="call-label">Call us for an appointment</p>
  <p class="call-number">(555) 018-2740</p>

  <div class="new-clients">We are accepting new clients!!</div>

  <footer class="footer">
    <div class="footer-item address">
      <svg viewBox="0 0 16 16"><path d="M8 1a5 5 0 0 0-5 5c0 4 5 9 5 9s5-5 5-9a5 5 0 0 0-5-5zm0 7a2 2 0 1 1 0-4 2 2 0 0 1 0 4z" fill="var(--white)"/></svg>
      <span>4180 Linden Ave., Suite 210-140, Fairhaven, CA 95000</span>
    </div>
    <div class="footer-item email">
      <svg viewBox="0 0 16 16"><rect x="1" y="3" width="14" height="10" rx="1" fill="var(--white)"/><path d="M1.5 3.8 8 9l6.5-5.2" fill="none" stroke="var(--brand-blue)" stroke-width="1.3"/></svg>
      <span>hello@pemberlytax.com</span>
    </div>
  </footer>

</div>
</body>
</html>
```